LOGO DESIGN: Construction Related Service Business

We require a logo for our business Tovar Services. We are a construction related business offering a range of services including machine services for groundworks (digging trenches, soak wells, preparing land for construction etc), demolition and truck haulage from demolition sites.
We would like our logo to be predominately text, but may include abstract graphics. The colour scheme should be mainly a mid bright blue and overall be quite 'clean'.

Industry/Entity Type

Construction

Contact Information for Business Card

Dale Morrow
Ph:041 592 3068
tovarservices@quillnet.com.au

Colors
0456a3

```html
<!DOCTYPE html>
<html lang="en">
<head>
<meta charset="utf-8">
<title>Dale Morrow – Tovar Services Business Card</title>
<link rel="stylesheet" href="https://fonts.googleapis.com/css2?family=Source+Sans+3:wght@400;700&display=swap">
<style>
  :root {
    --panel-blue: #0d5a7e;
    --panel-blue-light: #156a92;
    --ink: #333133;
    --rule: #2e2e30;
    --brand-blue: #0456a3;
    --paper: #ffffff;
    --side-band: #333133;
  }
  * { margin: 0; padding: 0; box-sizing: border-box; }
  html, body {
    width: 1200px;
    height: 720px;
    overflow: hidden;
    background: var(--paper);
  }
  .card {
    position: relative;
    width: 1200px;
    height: 720px;
    background: var(--paper);
    font-family: "Source Sans 3", "Myriad Pro", Arial, sans-serif;
    color: var(--ink);
  }
  .texture-panel {
    position: absolute;
    left: 0; top: 0;
    width: 428px;
    height: 720px;
    background: linear-gradient(135deg, var(--panel-blue-light), var(--panel-blue));
  }
  .side-band {
    position: absolute;
    right: 0; top: 0;
    width: 80px;
    height: 720px;
    background: var(--side-band);
  }
  .holder-name {
    position: absolute;
    left: 524px;
    top: 90px;
    font-size: 66px;
    line-height: 1;
    letter-spacing: -1.5px;
    font-weight: 400;
    white-space: nowrap;
  }
  .holder-name .given { font-weight: 700; }
  .rule {
    position: absolute;
    left: 523px;
    width: 554px;
    height: 2px;
    background: var(--rule);
  }
  .rule--top { top: 228px; }
  .rule--bottom { top: 392px; }
  .brand {
    position: absolute;
    left: 523px;
    top: 229px;
    width: 554px;
    height: 163px;
    display: flex;
    align-items: center;
    justify-content: center;
    gap: 16px;
  }
  .brand-dot {
    width: 40px;
    height: 40px;
    border-radius: 50%;
    background: var(--brand-blue);
  }
  .brand-name {
    font-size: 36px;
    font-weight: 700;
    letter-spacing: 1px;
    color: var(--brand-blue);
    text-transform: uppercase;
  }
  .contacts {
    position: absolute;
    left: 523px;
    top: 488px;
    list-style: none;
  }
  .contact-item {
    display: flex;
    align-items: center;
    height: 44px;
    font-size: 28px;
    white-space: nowrap;
  }
  .contact-icon {
    width: 36px;
    height: 30px;
    margin-right: 18px;
    flex-shrink: 0;
  }
</style>
</head>
<body>
  <div class="card">
    <div class="texture-panel" role="img" aria-label="Blue panel with fine diagonal stripe texture"></div>

    <h1 class="holder-name"><span class="given">Dale</span> Morrow</h1>

    <div class="rule rule--top"></div>
    <div class="brand">
      <span class="brand-dot"></span>
      <span class="brand-name">Tovar Services</span>
    </div>
    <div class="rule rule--bottom"></div>

    <ul class="contacts">
      <li class="contact-item">
        <svg class="contact-icon" viewBox="0 0 36 30" aria-hidden="true">
          <path d="M2 10 Q18 -2 34 10 L34 13 L27 13 L26 9 Q18 6 10 9 L9 13 L2 13 Z" fill="var(--ink)"/>
          <path d="M11 11 L25 11 L32 28 L4 28 Z" fill="var(--ink)"/>
          <g fill="var(--paper)">
            <rect x="13" y="15" width="2.4" height="2.4"/><rect x="17" y="15" width="2.4" height="2.4"/><rect x="21" y="15" width="2.4" height="2.4"/>
            <rect x="12.5" y="19" width="2.4" height="2.4"/><rect x="17" y="19" width="2.4" height="2.4"/><rect x="21.5" y="19" width="2.4" height="2.4"/>
            <rect x="12" y="23" width="2.4" height="2.4"/><rect x="17" y="23" width="2.4" height="2.4"/><rect x="22" y="23" width="2.4" height="2.4"/>
          </g>
        </svg>
        <span>041 592 3068</span>
      </li>
      <li class="contact-item">
        <svg class="contact-icon" viewBox="0 0 36 30" aria-hidden="true">
          <rect x="1" y="2" width="34" height="26" rx="2" fill="var(--ink)"/>
          <path d="M3 4 L18 17 L33 4 M3 26 L14 14 M33 26 L22 14" stroke="var(--paper)" stroke-width="1.6" fill="none"/>
        </svg>
        <span>tovarservices@quillnet.com.au</span>
      </li>
    </ul>

    <div class="side-band"></div>
  </div>
</body>
</html>
```